Clean Plinth Ads Banner Design For A Finance Company

Hi,
We're a UK based finance company and are looking for new banner ads to use on the Plinth Display Network.
We want the end product to stand out by using strong, minimal design - ideally starting from a dark theme, although I'm open to ideas.
The copy should read:
'Fast Bridging Loans From 0.39% PM'
Once we have these designs agreed, we are looking to replicate them for other products, changing only the text on each ad - for example, 'commercial mortgage service you can rely on' or 'development finance service you can rely on'.
The colours used on our website are the following:
Black - #040303
Orange - #f79124
White - #ffffff
Grey - #ffffff
Example ads that I like - https://www.brimcastle.com/wp-content/uploads/2021/07/plinth-display-ads-example-2-final.png.webp
2 - https://quendrahub.com/wp-content/uploads/2020/03/fbdd56ba3bd16c7a8debb13a411de786.jpg

```html
<!DOCTYPE html>
<html lang="en">
<head>
<meta charset="utf-8">
<title>Quillmont Finance – Bridging Loan Display Banners</title>
<link rel="stylesheet" href="https://fonts.googleapis.com/css2?family=Open+Sans:wght@300;400;600;700&display=swap">
<style>
  :root {
    --ink: #231f20;
    --black: #040303;
    --orange: #f79124;
    --white: #ffffff;
    --photo-warm: #6b5a48;
    --photo-cool: #1d2f33;
  }
  * { box-sizing: border-box; margin: 0; padding: 0; }
  html, body {
    width: 1200px; height: 1200px; overflow: hidden;
    background: var(--white);
    font-family: "Open Sans", Arial, sans-serif;
  }
  .board {
    position: relative; width: 1000px; height: 1000px;
    transform: scale(1.2); transform-origin: 0 0;
  }
  .banner {
    position: absolute; overflow: hidden;
    background: var(--ink); color: var(--white);
  }
  .banner-art { position: absolute; inset: 0; }
  .brand {
    position: absolute; text-align: center;
    color: var(--orange); font-weight: 700; line-height: 1.05;
  }
  .headline, .offer {
    position: absolute; text-align: center; font-weight: 300;
  }
  .headline b, .offer b { font-weight: 700; color: var(--orange); }
  .cta {
    position: absolute; display: flex; align-items: center; justify-content: center;
    background: var(--orange); color: var(--ink); border-radius: 999px;
    font-weight: 700; letter-spacing: 0.12em; text-transform: uppercase;
  }
  .divider {
    position: absolute; height: 0;
    border-top: 3px dotted var(--white);
  }

  /* 728 x 90 leaderboard */
  .leaderboard { left: 25px; top: 29px; width: 728px; height: 90px; }
  .leaderboard .brand { left: 8px; top: 25px; width: 150px; font-size: 20px; }
  .leaderboard .headline { left: 180px; top: 12px; width: 276px; font-size: 24px; line-height: 29px; }
  .leaderboard .offer { left: 470px; top: 10px; width: 140px; font-size: 18px; line-height: 22px; }
  .leaderboard .cta { left: 611px; top: 33px; width: 100px; height: 25px; font-size: 9.5px; }

  /* 160 x 600 skyscraper */
  .skyscraper { left: 25px; top: 149px; width: 160px; height: 600px; }
  .skyscraper .brand { left: 0; top: 14px; width: 160px; font-size: 24px; }
  .skyscraper .headline { left: 0; top: 130px; width: 160px; font-size: 28px; line-height: 30px; }
  .skyscraper .offer { left: 0; top: 414px; width: 160px; font-size: 22px; line-height: 29px; }
  .skyscraper .cta { left: 11px; top: 549px; width: 137px; height: 35px; font-size: 13px; }

  /* 336 x 280 rectangles */
  .rectangle { left: 206px; width: 336px; height: 280px; }
  .rectangle-dark { top: 149px; }
  .rectangle-accent { top: 469px; }
  .rectangle .brand { left: 0; width: 170px; font-size: 20px; }
  .rectangle-dark .brand { top: 14px; }
  .rectangle-accent .brand { top: 16px; color: var(--white); }
  .rectangle .headline, .rectangle .offer { left: 0; width: 172px; font-size: 18px; line-height: 21.5px; }
  .rectangle-dark .headline { top: 76px; }
  .rectangle-dark .divider { top: 150px; left: 25px; width: 126px; }
  .rectangle-dark .offer { top: 160px; }
  .rectangle-dark .cta { top: 239px; }
  .rectangle-accent .headline { top: 82px; }
  .rectangle-accent .divider { top: 156px; left: 25px; width: 126px; }
  .rectangle-accent .offer { top: 166px; }
  .rectangle-accent .cta { top: 242px; }
  .rectangle .cta { left: 36px; width: 100px; height: 24px; font-size: 9.5px; }
</style>
</head>
<body>
<div class="board">

  <section class="banner leaderboard">
    <svg class="banner-art" width="728" height="90" viewBox="0 0 728 90">
      <defs>
        <linearGradient id="photo-lb" x1="0" y1="0" x2="1" y2="1">
          <stop offset="0" stop-color="var(--photo-warm)"/>
          <stop offset="1" stop-color="var(--photo-cool)"/>
        </linearGradient>
      </defs>
      <path role="img" aria-label="Photo of a wooden model house with keys, darkened" d="M200 0 L463 0 L463 90 L185 90 Q168 45 200 0 Z" fill="url(#photo-lb)" opacity="0.55"/>
      <path d="M200 0 Q168 45 185 90" fill="none" stroke="var(--orange)" stroke-width="3"/>
    </svg>
    <div class="brand">Quillmont<br>Finance</div>
    <p class="headline"><b>Bridging</b> Loan Service<br>You Can Rely On</p>
    <p class="offer"><b>5★ Rated<br>Service</b> &amp;<br>No Broker Fees</p>
    <a class="cta">Learn More</a>
  </section>

  <section class="banner skyscraper">
    <svg class="banner-art" width="160" height="600" viewBox="0 0 160 600">
      <defs>
        <linearGradient id="photo-sky" x1="0" y1="0" x2="0" y2="1">
          <stop offset="0" stop-color="var(--photo-warm)"/>
          <stop offset="1" stop-color="var(--photo-cool)"/>
        </linearGradient>
      </defs>
      <path role="img" aria-label="Photo of a wooden model house with keys, darkened" d="M0 100 Q80 82 160 90 L160 372 Q80 418 0 398 Z" fill="url(#photo-sky)" opacity="0.6"/>
      <path d="M0 100 Q80 82 160 90" fill="none" stroke="var(--orange)" stroke-width="4"/>
    </svg>
    <div class="brand">Quillmont<br>Finance</div>
    <p class="headline"><b>Bridging</b><br>Loan<br>Service<br>You Can<br>Rely On</p>
    <p class="offer"><b>5★ Rated<br>Service</b> &amp;<br>No Broker<br>Fees</p>
    <a class="cta">Learn More</a>
  </section>

  <section class="banner rectangle rectangle-dark">
    <svg class="banner-art" width="336" height="280" viewBox="0 0 336 280">
      <defs>
        <linearGradient id="photo-rect-a" x1="0" y1="0" x2="1" y2="1">
          <stop offset="0" stop-color="var(--photo-warm)"/>
          <stop offset="1" stop-color="var(--photo-cool)"/>
        </linearGradient>
      </defs>
      <path role="img" aria-label="Photo of a wooden model house with keys" d="M192 0 L336 0 L336 280 L210 280 Q160 140 192 0 Z" fill="url(#photo-rect-a)"/>
      <path d="M192 0 Q160 140 210 280" fill="none" stroke="var(--orange)" stroke-width="4"/>
    </svg>
    <div class="brand">Quillmont<br>Finance</div>
    <p class="headline"><b>Bridging</b> Loan<br>Service You<br>Can Rely On</p>
    <div class="divider"></div>
    <p class="offer"><b>5★ Rated<br>Service</b> &amp;<br>No Broker Fees</p>
    <a class="cta">Learn More</a>
  </section>

  <section class="banner rectangle rectangle-accent">
    <svg class="banner-art" width="336" height="280" viewBox="0 0 336 280">
      <defs>
        <linearGradient id="photo-rect-b" x1="0" y1="0" x2="1" y2="1">
          <stop offset="0" stop-color="var(--photo-warm)"/>
          <stop offset="1" stop-color="var(--photo-cool)"/>
        </linearGradient>
      </defs>
      <rect x="0" y="0" width="180" height="71" fill="var(--orange)"/>
      <path role="img" aria-label="Photo of a wooden model house with keys" d="M192 0 L336 0 L336 280 L210 280 Q160 140 192 0 Z" fill="url(#photo-rect-b)"/>
      <path d="M192 0 Q160 140 210 280" fill="none" stroke="var(--orange)" stroke-width="4"/>
    </svg>
    <div class="brand">Quillmont<br>Finance</div>
    <p class="headline"><b>Bridging</b> Loan<br>Service You<br>Can Rely On</p>
    <div class="divider"></div>
    <p class="offer"><b>5★ Rated<br>Service</b> &amp;<br>No Broker Fees</p>
    <a class="cta">Learn More</a>
  </section>

</div>
</body>
</html>
```